Request for Business Card Design

Hi. My name is Marlena, I am looking for a new business card design for my company, Quorvane Sensing Systems, LLC. I really like the design you did for Tessaly Harvest and was hoping you could do something similar using our full logo and our mark. I am also open to any raised texture design using our mark. I have attached our full logo, which would need to be somewhere on the card, as well as the mark in both outline and full form, as well as our brand colors / guide. The card does not have to be white, as long as our logo and mark appear. I actually like darker colored business cards more, but am open to all options. If you are interested in working with me, please let me know. We would also take the business card design into letterhead design if you can do that.

```html
<!DOCTYPE html>
<html lang="en">
<head>
<meta charset="utf-8">
<title>Quorvane Sensing Systems — Business Card</title>
<link rel="stylesheet" href="https://fonts.googleapis.com/css2?family=Barlow:wght@400;500;600;700&display=swap">
<style>
  :root {
    --stage: #d4d6d9;
    --card-white: #ffffff;
    --charcoal: #3d3e41;
    --ink: #38393c;
    --brand-blue: #1a9ac9;
    --soft-text: #e6e7e9;
  }
  * { margin: 0; padding: 0; box-sizing: border-box; }
  html, body { width: 1200px; height: 876px; overflow: hidden; }
  body {
    background: var(--stage);
    font-family: "Barlow", Arial, sans-serif;
    color: var(--ink);
    position: relative;
  }
  .card {
    position: absolute;
    top: 290px;
    width: 520px;
    height: 297px;
    overflow: hidden;
    background: var(--card-white);
    box-shadow: 0 6px 18px rgba(0,0,0,0.18);
  }
  .card--front { left: 60px; }
  .card--back { left: 620px; background: var(--charcoal); }

  .band { position: absolute; left: 0; width: 100%; }
  .rule { position: absolute; left: 0; width: 100%; height: 2px; background: var(--brand-blue); }

  /* front */
  .front__band { top: 112px; height: 130px; background: var(--charcoal); }
  .front__rule--top { top: 106px; }
  .front__rule--bottom { top: 248px; }

  .brand {
    position: absolute;
    display: flex;
    align-items: center;
    gap: 14px;
  }
  .brand__dot {
    width: 46px; height: 46px; border-radius: 50%;
    background: var(--brand-blue);
    flex: none;
  }
  .brand__name {
    font-weight: 700;
    font-size: 30px;
    line-height: 1;
    letter-spacing: 1px;
    text-transform: uppercase;
    color: var(--ink);
  }
  .card--front .brand { top: 30px; left: 130px; }
  .card--back .brand { top: 122px; left: 92px; }

  .contact { position: absolute; top: 128px; left: 22px; color: var(--soft-text); }
  .contact__name {
    font-weight: 600; font-size: 19px; letter-spacing: 0.5px;
    color: var(--brand-blue); text-transform: uppercase;
  }
  .contact__title { font-size: 12px; margin-top: 1px; }
  .contact__line {
    display: flex; align-items: center; gap: 6px;
    font-size: 12.5px; letter-spacing: 1px; margin-top: 9px;
  }
  .contact__line + .contact__line { margin-top: 5px; }
  .icon { width: 10px; height: 10px; flex: none; }
  .contact__sep { margin-left: 10px; }

  .address {
    position: absolute; right: 92px; top: 186px;
    color: var(--soft-text); font-size: 13px; line-height: 1.35;
    letter-spacing: 1px; text-align: right;
  }
  .social { position: absolute; right: 22px; top: 196px; display: flex; gap: 8px; }
  .social__square { width: 22px; height: 22px; background: var(--brand-blue); }

  .web {
    position: absolute; top: 262px; left: 22px;
    display: flex; align-items: center; gap: 6px;
    font-size: 12.5px; letter-spacing: 0.8px; color: var(--ink);
  }

  /* back */
  .back__band { top: 92px; height: 110px; background: var(--card-white); }
  .back__rule--top { top: 86px; }
  .back__rule--bottom { top: 208px; }
</style>
</head>
<body>

  <section class="card card--front" aria-label="Business card front">
    <div class="brand">
      <span class="brand__dot"></span>
      <span class="brand__name">Quorvane Sensing Systems</span>
    </div>

    <div class="rule front__rule--top"></div>
    <div class="band front__band"></div>
    <div class="rule front__rule--bottom"></div>

    <div class="contact">
      <p class="contact__name">Elias Varnholt</p>
      <p class="contact__title">President</p>
      <p class="contact__line">
        <svg class="icon" viewBox="0 0 10 10"><path d="M2 0.5 L4 2.8 L3 4 Q4.5 6 6 7 L7.2 6 L9.5 8 L8.2 9.5 Q4 9 0.5 1.8 Z" fill="#1a9ac9"/></svg>
        555 014 2231
        <svg class="icon contact__sep" viewBox="0 0 10 10"><rect x="2.5" y="0.5" width="5" height="9" rx="1" fill="#1a9ac9"/></svg>
        555 014 7780
      </p>
      <p class="contact__line">
        <svg class="icon" viewBox="0 0 10 10"><rect x="0.5" y="2" width="9" height="6.5" fill="#1a9ac9"/><path d="M0.5 2 L5 5.8 L9.5 2" stroke="#3d3e41" stroke-width="1" fill="none"/></svg>
        info@quorvanesensing.com
      </p>
    </div>

    <p class="address">1180 Ridgeline Court<br>Fernhollow, CO 80999</p>
    <div class="social" aria-label="Social profiles">
      <span class="social__square"></span>
      <span class="social__square"></span>
    </div>

    <p class="web">
      <svg class="icon" viewBox="0 0 10 10"><circle cx="5" cy="5" r="4.3" fill="none" stroke="#1a9ac9" stroke-width="1.2"/><path d="M0.7 5 H9.3 M5 0.7 V9.3" stroke="#1a9ac9" stroke-width="1"/></svg>
      www.quorvanesensing.com
    </p>
  </section>

  <section class="card card--back" aria-label="Business card back">
    <div class="rule back__rule--top"></div>
    <div class="band back__band"></div>
    <div class="rule back__rule--bottom"></div>
    <div class="brand">
      <span class="brand__dot"></span>
      <span class="brand__name">Quorvane Sensing Systems</span>
    </div>
  </section>

</body>
</html>
```